Corporate Two Sided Business Card

Looking for a Corporate "edgy" Modern look and feel for a business card

We are looking at two options. Dark background with our logo on it, white background with our logo on it - The background is more - Charcoal / Graphite then black

Details will be

Rosalind Tebb

Licensee / Director

m. 0452 918 604

e. rosalind@quarvelhome.com.au

quarvelhome.com.au

Target Market(s)

Professional Business people that refer use business and clients that own Investment Properties

Industry/Entity Type

Business

Contact Information for Business Card

Details will be

Rosalind Tebb

Licensee / Director

m. 0452 918 604

quarvelhome.com.au

Font styles to use
Serif

Colors
000000
ec1f27
eeeeee
ffffff

Requirements
Must have
• Two options - White Background and Dark Background. - Two sided
Nice to have
• A design that is edgy, modern and new to look instead of boring style corporate cards - It should be a full integrated design
Should not have
• Block looking - Cheap.

```html
<!DOCTYPE html>
<html lang="en">
<head>
<meta charset="utf-8">
<title>Quarvelhome Business Card</title>
<link rel="stylesheet" href="https://fonts.googleapis.com/css2?family=Source+Sans+3:wght@400;600&display=swap">
<style>
  :root {
    --stage: #000000;
    --card: #2f3033;
    --ink: #ffffff;
    --ink-soft: #e6e6e6;
    --rule: #55575b;
  }
  * { margin: 0; padding: 0; box-sizing: border-box; }
  html, body { width: 1200px; height: 900px; overflow: hidden; background: var(--stage); }
  body { position: relative; font-family: "Source Sans 3", "Myriad Pro", Arial, sans-serif; color: var(--ink); }

  .card {
    position: absolute;
    top: 271px;
    width: 457px;
    height: 281px;
    border-radius: 12px;
    background: var(--card);
  }
  .card--front { left: 137px; }
  .card--back { left: 626px; }

  .front__brand {
    position: absolute;
    left: 188px; left: 48px;
    top: 118px;
    width: 160px;
    display: flex;
    align-items: center;
    gap: 8px;
    font-weight: 600;
    font-size: 21px;
    letter-spacing: 0.2px;
    color: var(--ink);
  }
  .front__brand-mark {
    width: 12px; height: 12px; background: var(--ink);
  }

  .front__divider {
    position: absolute;
    left: 205px;
    top: 67px;
    width: 1px;
    height: 150px;
    background: linear-gradient(to bottom, transparent, var(--rule) 15%, var(--rule) 85%, transparent);
  }

  .front__details { position: absolute; left: 234px; top: 72px; }
  .front__name { font-weight: 600; font-size: 17px; line-height: 20px; }
  .front__role { font-size: 13px; line-height: 18px; color: var(--ink-soft); }

  .contact-list { list-style: none; margin-top: 22px; }
  .contact-list li {
    display: flex; align-items: center; gap: 6px;
    font-size: 13px; line-height: 19px; color: var(--ink-soft);
  }
  .contact-list svg { width: 10px; height: 10px; fill: var(--ink); flex: none; }

  .back__brand {
    position: absolute;
    inset: 0;
    display: flex; align-items: center; justify-content: center;
    gap: 12px;
    font-weight: 600;
    font-size: 46px;
    letter-spacing: 0.3px;
    color: var(--ink);
    padding-bottom: 4px;
  }
  .back__brand-mark { width: 20px; height: 20px; background: var(--ink); }
</style>
</head>
<body>
  <section class="card card--front" aria-label="Business card front">
    <div class="front__brand"><span class="front__brand-mark"></span>quarvelhome</div>
    <div class="front__divider"></div>
    <div class="front__details">
      <p class="front__name">Rosalind Tebb</p>
      <p class="front__role">Licensee / Director</p>
      <ul class="contact-list">
        <li>
          <svg viewBox="0 0 10 10" aria-hidden="true"><path d="M2 0.5 L3.6 2.4 L2.8 3.5 C3.4 4.8 4.9 6.4 6.4 7.1 L7.5 6.3 L9.5 8 L8.4 9.5 C4.5 9.2 0.8 5.4 0.5 1.6 Z"/></svg>
          0452 918 604
        </li>
        <li>
          <svg viewBox="0 0 10 10" aria-hidden="true"><path d="M0.5 2 H9.5 V8.5 H0.5 Z M1.2 2.6 L5 5.6 L8.8 2.6 V3.4 L5 6.4 L1.2 3.4 Z" fill-rule="evenodd"/></svg>
          rosalind@quarvelhome.com.au
        </li>
        <li>
          <svg viewBox="0 0 10 10" aria-hidden="true"><circle cx="5" cy="5" r="4.5"/></svg>
          www.quarvelhome.com.au
        </li>
      </ul>
    </div>
  </section>

  <section class="card card--back" aria-label="Business card back">
    <div class="back__brand"><span class="back__brand-mark"></span>quarvelhome</div>
  </section>
</body>
</html>
```